Torvik & Associates - 3rd Party Logistics Company

Torvik & Associates is a 3rd Party Logistics Company established in 1995 located in St. Louis, MO USA. We are a non asset based transportation company that works with our clients to move their freight and help them manage their supply chain. We are looking for a brochure about our company and services. We are able to provide our customers with shipment entry and rating tools along with visibility of all their shipments thought our cloud based TMS build on CloudNest's Pelzo.com platform. Through our TMS application we also provide customized reports, KPI and dashboards specific to the clients needs and wants. This marketing material would be left behind after a call or with the receptionist to pass along to the appropriate person. Looking for something that is eye catching that in a glance could tell someone who we are and what we do. Our website is www.torvikltd-example.com. I attached our logo and powerpoint.

Target Market(s)

Manufacturing Companies or any company that does any type of shipping in North Americana.

Industry/Entity Type

Logistic

Requirements
Nice to have
• We would like the brochure to be a bi-fold.. I have attached a few examples I found on the internet

```html
<!DOCTYPE html>
<html lang="en">
<head>
<meta charset="utf-8">
<title>Torvik &amp; Associates – Bi-fold Brochure</title>
<link href="https://fonts.googleapis.com/css2?family=Roboto+Condensed:wght@700&family=Arimo:wght@400;700&display=swap" rel="stylesheet">
<style>
  :root{
    --navy:#27378f;
    --green:#3a9a3f;
    --lavender:#8d90c8;
    --paper:#e7e8ea;
    --ink:#333438;
    --black:#111;
    --white:#ffffff;
    --stage:#ffffff;
  }
  *{box-sizing:border-box;margin:0;padding:0}
  html,body{width:1200px;height:1200px;overflow:hidden;background:var(--stage)}
  body{position:relative;font-family:"Arimo",Arial,sans-serif;color:var(--ink)}

  .spread{position:absolute;left:50px;width:1100px;height:550px;background:var(--paper);overflow:hidden}
  .spread--outside{top:40px}
  .spread--inside{top:610px}
  .spread-art{position:absolute;inset:0;width:1100px;height:550px}

  .section-tab{position:absolute;background:var(--navy);color:var(--white);
    font-family:"Roboto Condensed",Arial,sans-serif;font-weight:700;font-size:27px;
    letter-spacing:.5px;line-height:1;padding:6px 18px 5px 34px}

  .body-col{position:absolute;font-size:9.6px;line-height:1.22;color:var(--ink)}
  .body-col p + p{margin-top:12px}

  /* outside spread */
  .tech-tab{left:0;top:176px}
  .tech-col-1{left:48px;top:228px;width:205px}
  .tech-col-2{left:272px;top:228px;width:195px}

  .headline{position:absolute;right:40px;top:160px;display:flex;flex-direction:column;align-items:flex-end;
    font-family:"Roboto Condensed",Arial,sans-serif;font-weight:700;color:var(--black)}
  .headline-row{display:flex;align-items:baseline;gap:10px;line-height:.95}
  .headline .lead{font-size:28px}
  .headline .key{font-size:44px;color:var(--navy)}

  .brand-name{position:absolute;left:590px;top:500px;font-family:"Arimo",Arial,sans-serif;
    font-weight:700;font-size:22px;color:var(--navy);letter-spacing:.5px;display:flex;align-items:center;gap:8px}
  .brand-name .mark{width:14px;height:14px;background:var(--navy)}

  /* inside spread */
  .about-tab{left:0;top:38px}
  .about-col-1{left:52px;top:92px;width:200px}
  .about-col-2{left:270px;top:80px;width:205px}

  .services-tab{left:548px;top:30px}
  .services-intro{position:absolute;left:580px;top:82px;width:480px;font-size:10px;line-height:1.25}
  .service-group{position:absolute;font-size:10px;line-height:1.6}
  .service-group h3{font-family:"Arimo",Arial,sans-serif;font-weight:700;font-size:11.5px;color:var(--navy);margin-bottom:1px}
  .service-list{list-style:none}
  .service-list li{position:relative;padding-left:24px}
  .service-list li::before{content:"";position:absolute;left:2px;top:4px;width:8px;height:8px;border-radius:50%;background:var(--green)}
  .service-list li::after{content:"";position:absolute;left:4px;top:7px;width:3px;height:2px;background:var(--white)}
  .group-transport{left:580px;top:140px}
  .group-logistics{left:820px;top:128px}

  .train-art{position:absolute;left:20px;top:345px;width:440px;height:195px;border-radius:18px 30px 0 0;
    background:linear-gradient(180deg,#2f8fd0 0%,#2474b4 55%,#e8b420 75%,#2a2a2a 100%)}
  .photo-circle{position:absolute;border-radius:50%;border:4px solid var(--white);box-shadow:0 2px 6px rgba(0,0,0,.25)}
  .circle-train{left:690px;top:300px;width:160px;height:160px;background:radial-gradient(circle at 50% 40%,#3d6c93,#1a2d45 60%,#3b6f2a)}
  .circle-globe{left:850px;top:318px;width:170px;height:170px;background:radial-gradient(circle at 45% 40%,#7fc4ff,#1f4fa0 45%,#0c1c3d 80%)}
  .circle-plane{left:760px;top:400px;width:140px;height:140px;background:linear-gradient(180deg,#3b2a4a,#c2502a 60%,#f0a040)}
  .circle-ship{left:655px;top:425px;width:110px;height:110px;background:linear-gradient(180deg,#c9d8e8,#7a95b0 50%,#c2302a 75%,#2a4a6a)}
</style>
</head>
<body>

<section class="spread spread--outside">
  <svg class="spread-art" viewBox="0 0 1100 550">
    <defs>
      <linearGradient id="techPhoto" x1="0" y1="0" x2="1" y2="1">
        <stop offset="0" stop-color="#5a2a2a"/>
        <stop offset=".45" stop-color="#2e5fa8"/>
        <stop offset="1" stop-color="#1d3350"/>
      </linearGradient>
      <linearGradient id="travelPhoto" x1="0" y1="0" x2="1" y2="0">
        <stop offset="0" stop-color="#6d8a63"/>
        <stop offset=".5" stop-color="#d9d6cc"/>
        <stop offset="1" stop-color="#e6e4de"/>
      </linearGradient>
    </defs>
    <g role="img" aria-label="Photo: glowing digital globe held over a hand">
      <path d="M0,0 H550 V255 C480,185 300,150 0,158 Z" fill="url(#techPhoto)"/>
    </g>
    <path d="M0,158 C300,150 480,185 550,255" fill="none" stroke="var(--navy)" stroke-width="16"/>
    <g role="img" aria-label="Illustration: passenger jet flying past a green globe">
      <path d="M550,0 H1100 V150 C900,160 700,195 555,255 Z" fill="url(#travelPhoto)"/>
    </g>
    <path d="M555,255 C700,195 900,160 1100,150" fill="none" stroke="var(--navy)" stroke-width="16"/>

    <path d="M556,240 C620,395 820,445 1100,438 V472 C800,472 610,385 556,240 Z" fill="var(--green)"/>
    <path d="M556,240 C610,385 800,472 1100,472 V550 H300 C440,505 530,410 556,240 Z" fill="var(--navy)"/>
    <path d="M0,478 C150,490 280,500 380,530 L370,550 H0 Z" fill="var(--lavender)"/>
    <path d="M0,500 C150,508 290,520 360,550 H0 Z" fill="var(--navy)"/>
    <path d="M370,550 C470,505 600,478 740,482 C870,488 960,525 1010,550 Z" fill="var(--lavender)"/>
    <path d="M390,550 C490,512 610,490 740,494 C860,500 950,530 990,550 Z" fill="var(--white)"/>
  </svg>

  <h2 class="section-tab tech-tab">TECHNOLOGY</h2>
  <div class="body-col tech-col-1">
    <p>Torvik &amp; Associates' transportation management software (TMS) offers a full suite of transportation and logistics services. Built on the Pelzo.com platform, our TMS provides an integrated solution that streamlines shipment process with the absolute most efficient process available to date. This revolutionary cloud based technology allows us to customize our technology to your specific needs. The Pelzo.com platform will also allow Torvik &amp; Associates' clients the advantage of using their existing technology and easily integrate their ERP systems via EDI/XML. Client's that choose to outsource their logistics services to Torvik &amp; Associates are provided this cutting edge, cloud based software absolutely free of charge.</p>
    <p>Torvik's multi tenant platform provides customers, vendors and carriers real time visibility and</p>
  </div>
  <div class="body-col tech-col-2">
    <p>collaboration through the entire supply chain. Each Torvik &amp; Associates user's sensitive personal data is kept secure and insulated from that of other users, however each participant is represented in this virtual marketplace. Gathering all these users in one space affords greater collaboration, transparency, and integration, saving time and money for all involved. This software is unique in that is has been Developed and continuously maintained by veteran transportation professionals who fully understand the importance of improving process efficiencies while reducing costs.</p>
  </div>

  <h1 class="headline">
    <span class="headline-row"><span class="lead">USING</span></span>
    <span class="headline-row"><span class="key">TECHNOLOGY</span></span>
    <span class="headline-row"><span class="lead">TO ACHIEVE</span></span>
    <span class="headline-row"><span class="key">SUCCESS</span></span>
    <span class="headline-row"><span class="lead">THROUGH</span><span class="key">VISION</span></span>
    <span class="headline-row"><span class="lead">&amp;</span><span class="key">INNOVATION</span></span>
  </h1>

  <div class="brand-name"><span class="mark"></span>Torvik &amp; Associates</div>
</section>

<section class="spread spread--inside">
  <svg class="spread-art" viewBox="0 0 1100 550">
    <path d="M0,505 C200,465 350,385 550,405 C750,425 900,445 1100,325 V345 C900,465 750,445 550,425 C350,405 200,485 0,525 Z" fill="var(--green)"/>
    <path d="M0,525 C200,485 350,405 550,425 C750,445 900,465 1100,345 V550 H0 Z" fill="var(--navy)"/>
  </svg>

  <h2 class="section-tab about-tab">ABOUT US</h2>
  <div class="body-col about-col-1">
    <p>Torvik &amp; Associates is a non-asset based transportation logistics provider. This enables us to excel in an ever-changing business environment. Our professional staff has over 200 years of experience in the transportation industry. Our company has not only grown at a consistent double digit pace over the past 18 years but has remained a viable competitor in a volatile marketplace. Our financial sustainability has allowed us not only to gain the respect of the industry but has also given us the opportunity to partner with the best in class carriers.</p>
    <p>Torvik &amp; Associates was founded in 1995 by Mark &amp; Karen Torvik. The foundation of our company is to</p>
  </div>
  <div class="body-col about-col-2">
    <p>assist the client in cost reduction while improving speed, predictability and reliability of your transportation needs. This model of premiere customer service encompasses overall traffic patterns and performance across the entire supply chain. Torvik &amp; Associates leveraged CloudNest.com, the leader in cloud-based Customer Relationship Management (CRM), to launch proprietary web-based technology-enabled transportation and supply chain management software. Torvik &amp; Associates software as a service (SaaS) provides clients the tools necessary to revolutionize their current method of operations, increase efficiencies and economize freight spend overall.</p>
  </div>

  <div class="train-art" role="img" aria-label="Illustration: blue and yellow freight locomotive on rails"></div>

  <h2 class="section-tab services-tab">SERVICES</h2>
  <p class="services-intro">Torvik &amp; Associates' services are among the most competitive in the market. We offer you the flexibility to either fully outsource your transportation services or subscribe to our user-friendly technology.</p>

  <div class="service-group group-transport">
    <h3>Transportation:</h3>
    <ul class="service-list">
      <li>Air and Expedited Services</li>
      <li>Inter-Modal</li>
      <li>International</li>
      <li>Less than Truckload (LTL)</li>
      <li>Truckload</li>
    </ul>
  </div>
  <div class="service-group group-logistics">
    <h3>Logistics:</h3>
    <ul class="service-list">
      <li>Rate Negotiation</li>
      <li>Shipment Booking and Tracking</li>
      <li>Carrier Management and Compliance</li>
      <li>Customized Reporting</li>
      <li>Freight bill audit and payment</li>
      <li>Claim Processing</li>
      <li>Inbound Management</li>
    </ul>
  </div>

  <div class="photo-circle circle-train" role="img" aria-label="Photo: locomotive at dusk"></div>
  <div class="photo-circle circle-globe" role="img" aria-label="Photo: glowing globe above an open hand"></div>
  <div class="photo-circle circle-ship" role="img" aria-label="Photo: container ship at sea"></div>
  <div class="photo-circle circle-plane" role="img" aria-label="Photo: airplane taking off at sunset"></div>
</section>

</body>
</html>
```